Design a business card (front and back) for a Technology Consulting firm. Preference is for a clean look - professional, favour minimalist rather than something busy. two logos are attached. You can use any of them. . The information below is for the purpose of presenting an entry in the contest, but the winner will be given correct information to product another version of the entry. The winner will also be given an opportunity to prepare a letterhead (ideally consistent with the business card).

Mara Colvin
Partner
+61 438 902 617
+61 7 3986 2150
jane@[url removed, login to view]
[url removed, login to view]
GPO Box 8362
Brisbane QLD 4009

The winning entry should be in a format that most business card printers can easily print.

```html
<!DOCTYPE html>
<html lang="en">
<head>
<meta charset="utf-8">
<title>Norlane Consulting Services – Business Card</title>
<link rel="stylesheet" href="https://fonts.googleapis.com/css2?family=Roboto+Condensed:wght@400;700&family=Roboto:wght@400;500&display=swap">
<style>
  :root {
    --page-bg: #e4e4e4;
    --card-bg: #292523;
    --brand-red: #b83a26;
    --muted-grey: #6d6866;
    --soft-grey: #a9a4a1;
    --white: #ffffff;
  }
  * { box-sizing: border-box; margin: 0; padding: 0; }
  html, body { width: 1200px; height: 900px; overflow: hidden; }
  body {
    background: var(--page-bg);
    font-family: "Roboto", Arial, sans-serif;
    position: relative;
  }
  .card {
    position: absolute;
    left: 290px;
    width: 620px;
    height: 354px;
    background: var(--card-bg);
    box-shadow: 0 6px 18px rgba(0,0,0,0.25);
    overflow: hidden;
  }
  .card--details { top: 50px; }
  .card--brand { top: 496px; }

  .brand {
    position: absolute;
    display: flex;
    align-items: stretch;
    font-family: "Roboto Condensed", Arial, sans-serif;
  }
  .card--details .brand { left: 150px; top: 48px; }
  .card--brand .brand { left: 120px; top: 128px; }

  .brand__mark {
    color: var(--brand-red);
    font-weight: 700;
    font-size: 44px;
    letter-spacing: 1px;
    line-height: 1;
    padding-right: 14px;
    align-self: flex-start;
  }
  .brand__divider {
    width: 1px;
    background: var(--muted-grey);
    margin-top: 44px;
    height: 50px;
  }
  .brand__text {
    padding-left: 10px;
    padding-top: 44px;
    color: var(--muted-grey);
  }
  .brand__name {
    font-weight: 700;
    font-size: 22px;
    line-height: 1.05;
    text-transform: uppercase;
  }
  .brand__tagline {
    font-size: 10px;
    letter-spacing: 1px;
    text-transform: uppercase;
    margin-top: 3px;
    padding-bottom: 5px;
    border-bottom: 1px solid var(--muted-grey);
    width: 210px;
  }

  .tab-accent {
    position: absolute;
    left: 0;
    top: 92px;
    width: 30px;
    height: 18px;
    background: var(--white);
  }
  .person {
    position: absolute;
    left: 46px;
    top: 90px;
    color: var(--white);
  }
  .person__name {
    font-size: 15px;
    font-variant: small-caps;
    letter-spacing: 0.5px;
  }
  .person__role {
    font-size: 11px;
    font-variant: small-caps;
    color: var(--soft-grey);
    margin-top: 2px;
  }
  .person__address {
    font-size: 10px;
    color: var(--soft-grey);
    margin-top: 14px;
    line-height: 1.5;
  }

  .contact {
    position: absolute;
    right: 52px;
    bottom: 34px;
    list-style: none;
    color: var(--white);
    font-size: 11px;
    text-align: right;
  }
  .contact__item {
    display: flex;
    justify-content: flex-end;
    align-items: center;
    gap: 10px;
    line-height: 20px;
  }
  .contact__lines { line-height: 15px; }
  .contact__icon { width: 12px; height: 12px; flex: none; }
  .edge-accent {
    position: absolute;
    right: 0;
    bottom: 30px;
    width: 24px;
    height: 76px;
    background: var(--white);
  }
</style>
</head>
<body>

<section class="card card--details" aria-label="Business card, details side">
  <div class="brand">
    <div class="brand__mark">NORLANE</div>
    <div class="brand__divider"></div>
    <div class="brand__text">
      <div class="brand__name">Norlane Consulting<br>Services Ltd</div>
      <div class="brand__tagline">Spirit of Excellence</div>
    </div>
  </div>

  <div class="tab-accent"></div>
  <div class="person">
    <div class="person__name">Mara Colvin</div>
    <div class="person__role">Partner</div>
    <div class="person__address">GPO Box 8362<br>Brisbane QLD 4009</div>
  </div>

  <ul class="contact">
    <li class="contact__item">
      <span class="contact__lines">+61 438 902 617<br>+61 7 3986 2150</span>
      <svg class="contact__icon" viewBox="0 0 12 12" aria-hidden="true"><path d="M2.5 1h2l1 2.5-1.3 1a6 6 0 0 0 2.8 2.8l1-1.3L11 7v2a1 1 0 0 1-1 1A9 9 0 0 1 1.5 2 1 1 0 0 1 2.5 1z" fill="#a9a4a1"/></svg>
    </li>
    <li class="contact__item">
      <span>mara@norlaneconsult.com</span>
      <svg class="contact__icon" viewBox="0 0 12 12" aria-hidden="true"><rect x="1" y="2.5" width="10" height="7" fill="#a9a4a1"/><path d="M1 2.5l5 4 5-4" fill="none" stroke="#292523" stroke-width="1"/></svg>
    </li>
    <li class="contact__item">
      <span>www.norlaneconsult.com</span>
      <svg class="contact__icon" viewBox="0 0 12 12" aria-hidden="true"><g fill="none" stroke="#a9a4a1" stroke-width="1"><circle cx="6" cy="6" r="4.8"/><ellipse cx="6" cy="6" rx="2" ry="4.8"/><path d="M1.2 6h9.6"/></g></svg>
    </li>
  </ul>
  <div class="edge-accent"></div>
</section>

<section class="card card--brand" aria-label="Business card, brand side">
  <div class="brand">
    <div class="brand__mark">NORLANE</div>
    <div class="brand__divider"></div>
    <div class="brand__text">
      <div class="brand__name">Norlane Consulting<br>Services Ltd</div>
      <div class="brand__tagline">Spirit of Excellence</div>
    </div>
  </div>
</section>

</body>
</html>
```